Pelvane Global Media
Business Card. Letterhead and Envelope.
Pelvane Global Media  - Communications and Media
Creative Brief
Professional
Tomas Wyck-Field
Managing Director - Europe
Fenmoor House Ashbury Row Tillington Kent ME9 4QZ UK
tomas.wyckfield@pelvanemedia.example
www.pelvanemedia.example
I would like to see our logo plus a listing of our office locations included please. The office locations listed in upper case please but not in bold and not too big. They are: Amsterdam, London, Munich, New York, San Francisco.

```html
<!DOCTYPE html>
<html lang="en">
<head>
<meta charset="utf-8">
<title>Pelvane Global Media – Stationery</title>
<link rel="stylesheet" href="https://fonts.googleapis.com/css2?family=Montserrat:wght@400;600&family=Open+Sans:wght@400;600&display=swap">
<style>
  :root{
    --brand-blue:#1f74bb;
    --ink:#2b3440;
    --muted:#7a828c;
    --paper:#ffffff;
    --field:#eef0f3;
    --backdrop:#e4e6e9;
    --hairline:#d6dade;
  }
  *{box-sizing:border-box;margin:0;padding:0}
  html,body{width:1200px;height:921px;overflow:hidden}
  body{background:var(--backdrop);font-family:"Open Sans",Arial,sans-serif;color:var(--ink);position:relative}

  .sheet{position:absolute;background:var(--paper);box-shadow:0 4px 14px rgba(0,0,0,.12);overflow:hidden}
  .brand-band{position:absolute;left:0;right:0;bottom:0;background:var(--brand-blue)}

  .brand{display:flex;align-items:center;gap:8px}
  .brand-dot{width:20px;height:20px;border-radius:50%;background:var(--brand-blue);flex:none}
  .brand-name{font-family:"Montserrat",Arial,sans-serif;font-weight:600;letter-spacing:.3em;color:var(--ink);font-size:14px;line-height:1}
  .brand-tag{font-family:"Montserrat",Arial,sans-serif;font-weight:600;letter-spacing:.3em;color:var(--ink);font-size:5.5px;margin-top:3px}

  .small{font-size:7px;line-height:1.55;color:var(--muted)}
  .offices{font-size:5.5px;letter-spacing:.12em;text-transform:uppercase;color:var(--muted);font-weight:400;line-height:1.7}

  /* Business card front */
  .card-front{left:40px;top:40px;width:210px;height:124px}
  .card-front .brand{position:absolute;left:14px;top:16px}
  .card-front .contact{position:absolute;left:14px;top:54px}
  .card-front .person{font-size:8.5px;font-weight:600}
  .card-front .role{font-size:6.5px;color:var(--brand-blue);margin-bottom:3px}
  .card-front .small{font-size:6px;line-height:1.5}
  .card-front .brand-band{height:6px}

  /* Business card back */
  .card-back{left:270px;top:40px;width:210px;height:124px}
  .card-back .brand{position:absolute;left:50%;top:18px;transform:translateX(-50%)}
  .card-back .brand-band{height:60px;display:flex;align-items:center;justify-content:center;padding:0 12px;text-align:center}
  .card-back .offices{color:#fff}

  /* Large envelope front */
  .envelope-front{left:40px;top:194px;width:440px;height:250px}
  .envelope-front .brand{position:absolute;left:22px;top:22px}
  .envelope-front .return{position:absolute;left:22px;top:58px}
  .envelope-front .brand-band{height:8px}

  /* Envelope back */
  .envelope-back{left:40px;top:474px;width:440px;height:250px}
  .envelope-back svg{position:absolute;inset:0}

  /* Shared A4 sheet */
  .a4{top:40px;width:320px;height:453px;padding:26px 28px}
  .a4 .brand-band{height:7px}
  .sheet-footer{position:absolute;left:28px;right:28px;bottom:18px;border-top:1px solid var(--hairline);padding-top:6px}
  .sheet-footer .small{font-size:5.5px;margin-top:2px}

  /* Fax sheet */
  .fax{left:510px}
  .fax-title{position:absolute;right:28px;top:24px;font-family:"Montserrat",Arial,sans-serif;font-weight:600;font-size:22px;letter-spacing:.2em;color:var(--ink)}
  .fax-fields{margin-top:36px;display:grid;grid-template-columns:1fr 1fr;gap:6px 10px}
  .fax-field{display:flex;align-items:center;gap:6px;font-size:6.5px;color:var(--muted)}
  .fax-field span{width:30px;flex:none}
  .fax-field i{flex:1;height:14px;background:var(--field);border-radius:2px}
  .fax-checks{margin-top:16px;display:flex;gap:12px;font-size:6.5px;color:var(--muted)}
  .fax-checks label{display:flex;align-items:center;gap:4px}
  .fax-checks label::before{content:"";width:7px;height:7px;border:1px solid var(--muted)}
  .fax-notes{margin-top:16px;font-size:6.5px;color:var(--muted);border-top:1px solid var(--hairline);padding-top:6px}

  /* Letterhead */
  .letterhead{left:860px}
  .recipient{margin-top:30px;font-size:6.5px;line-height:1.6}
  .letter-date{margin-top:12px;font-size:6.5px}
  .letter-body{margin-top:12px;font-size:6.5px;line-height:1.7}
  .letter-body p{margin-bottom:8px}
  .signature{margin-top:8px;width:90px;height:24px;border-bottom:1px solid var(--hairline)}
  .signer{margin-top:4px;font-size:6.5px;line-height:1.5}
  .signer strong{font-weight:600}

  /* DL envelope */
  .envelope-dl{left:560px;top:530px;width:600px;height:300px}
  .envelope-dl .brand{position:absolute;left:26px;top:24px}
  .envelope-dl .return{position:absolute;left:26px;top:62px}
  .envelope-dl .brand-band{height:8px}
</style>
</head>
<body>

  <section class="sheet card-front" aria-label="Business card front">
    <div class="brand">
      <span class="brand-dot"></span>
      <div><div class="brand-name">PELVANE</div><div class="brand-tag">GLOBAL MEDIA</div></div>
    </div>
    <div class="contact">
      <div class="person">Tomas Wyck-Field</div>
      <div class="role">Managing Director - Europe</div>
      <div class="small">Fenmoor House Ashbury Row Tillington Kent ME9 4QZ UK<br>tomas.wyckfield@pelvanemedia.example<br>www.pelvanemedia.example</div>
    </div>
    <div class="brand-band"></div>
  </section>

  <section class="sheet card-back" aria-label="Business card back">
    <div class="brand">
      <span class="brand-dot"></span>
      <div><div class="brand-name">PELVANE</div><div class="brand-tag">GLOBAL MEDIA</div></div>
    </div>
    <div class="brand-band"><span class="offices">Amsterdam · London · Munich<br>New York · San Francisco</span></div>
  </section>

  <section class="sheet envelope-front" aria-label="Envelope front">
    <div class="brand">
      <span class="brand-dot"></span>
      <div><div class="brand-name">PELVANE</div><div class="brand-tag">GLOBAL MEDIA</div></div>
    </div>
    <div class="return small">Fenmoor House Ashbury Row Tillington Kent ME9 4QZ UK</div>
    <div class="brand-band"></div>
  </section>

  <section class="sheet envelope-back" aria-label="Envelope back">
    <svg width="440" height="250" viewBox="0 0 440 250">
      <path d="M0 0 L220 140 L440 0 Z" fill="var(--brand-blue)"/>
      <path d="M0 250 L186 118 M440 250 L254 118" stroke="var(--hairline)" stroke-width="1.2" fill="none"/>
    </svg>
  </section>

  <section class="sheet a4 fax" aria-label="Fax sheet">
    <div class="brand">
      <span class="brand-dot"></span>
      <div><div class="brand-name">PELVANE</div><div class="brand-tag">GLOBAL MEDIA</div></div>
    </div>
    <div class="fax-title">FAX</div>
    <div class="fax-fields">
      <div class="fax-field"><span>To</span><i></i></div>
      <div class="fax-field"><span>From</span><i></i></div>
      <div class="fax-field"><span>Fax</span><i></i></div>
      <div class="fax-field"><span>Pages</span><i></i></div>
      <div class="fax-field"><span>Phone</span><i></i></div>
      <div class="fax-field"><span>Date</span><i></i></div>
      <div class="fax-field"><span>Re</span><i></i></div>
      <div class="fax-field"><span>CC</span><i></i></div>
    </div>
    <div class="fax-checks">
      <label>Urgent</label><label>For Review</label><label>Please Reply</label><label>Please Recycle</label>
    </div>
    <div class="fax-notes">Comments</div>
    <footer class="sheet-footer">
      <div class="offices">Amsterdam · London · Munich · New York · San Francisco</div>
      <div class="small">Fenmoor House Ashbury Row Tillington Kent ME9 4QZ UK · www.pelvanemedia.example</div>
    </footer>
    <div class="brand-band"></div>
  </section>

  <section class="sheet a4 letterhead" aria-label="Letterhead">
    <div class="brand">
      <span class="brand-dot"></span>
      <div><div class="brand-name">PELVANE</div><div class="brand-tag">GLOBAL MEDIA</div></div>
    </div>
    <div class="recipient">Ada Linfield<br>Orchard Studio<br>12 Vale Street<br>Bristol BS1 4DJ</div>
    <div class="letter-date">14 March 2024</div>
    <div class="letter-body">
      <p>Dear Ms Linfield,</p>
      <p>Thank you for meeting our team last week. We were pleased to hear about your plans for the coming season and believe our studios can support each stage of the campaign.</p>
      <p>Please find the proposal enclosed with this letter. We look forward to your reply.</p>
      <p>Yours sincerely,</p>
    </div>
    <div class="signature"></div>
    <div class="signer"><strong>Tomas Wyck-Field</strong><br>Managing Director - Europe</div>
    <footer class="sheet-footer">
      <div class="offices">Amsterdam · London · Munich · New York · San Francisco</div>
      <div class="small">Fenmoor House Ashbury Row Tillington Kent ME9 4QZ UK · www.pelvanemedia.example</div>
    </footer>
    <div class="brand-band"></div>
  </section>

  <section class="sheet envelope-dl" aria-label="DL envelope front">
    <div class="brand">
      <span class="brand-dot"></span>
      <div><div class="brand-name">PELVANE</div><div class="brand-tag">GLOBAL MEDIA</div></div>
    </div>
    <div class="return small">Fenmoor House Ashbury Row Tillington Kent ME9 4QZ UK<br>www.pelvanemedia.example</div>
    <div class="brand-band"></div>
  </section>

</body>
</html>
```